Ferncrest Dental, LLC business card project

Business card to be designed with current logo.
Dental office- please keep design of card that looks clean and professional.
Please include the following info:
Ferncrest Dental, LLC
Dr. Lorna Pettigrew
2871 Marlowe Street
Harlow Ridge, VT 05999
555-555-0193
ferncrestdental.office@examplemail.test
Hello everyone-
Reason: Just got back from overseas- will look at all designs and provide feedback. Thank you!
Reason: Polling my friends for the final selection-
thank you to all those that participated- so many talented designers!

```html
<!DOCTYPE html>
<html lang="en">
<head>
<meta charset="utf-8">
<title>Ferncrest Dental, LLC – Business Card</title>
<link rel="stylesheet" href="https://fonts.googleapis.com/css2?family=Questrial&display=swap">
<style>
  :root {
    --lime: #b2d235;
    --lime-deep: #9cc42a;
    --leaf: #5c9e3a;
    --leaf-dark: #3f8a34;
    --text-soft: #86b93c;
    --rule: #cfe3a6;
    --paper: #ffffff;
    --backdrop: #eef0ec;
    --shadow: rgba(40, 60, 20, 0.18);
  }
  * { margin: 0; padding: 0; box-sizing: border-box; }
  html, body {
    width: 1200px;
    height: 759px;
    overflow: hidden;
    background: var(--backdrop);
    font-family: "Questrial", "Helvetica Neue", Arial, sans-serif;
  }
  .sheet {
    width: 1200px;
    height: 759px;
    display: flex;
    align-items: center;
    justify-content: center;
    gap: 36px;
  }
  .card {
    position: relative;
    width: 560px;
    height: 320px;
    box-shadow: 0 14px 30px var(--shadow);
    overflow: hidden;
  }

  /* Front */
  .card--front {
    background: var(--lime);
    display: flex;
    align-items: center;
    justify-content: center;
  }
  .brand {
    display: flex;
    align-items: center;
    gap: 12px;
  }
  .brand__dot {
    width: 14px;
    height: 14px;
    border-radius: 50%;
    background: currentColor;
  }
  .brand__name {
    font-size: 34px;
    letter-spacing: -0.5px;
    white-space: nowrap;
  }
  .card--front .brand { color: var(--paper); }

  /* Back */
  .card--back { background: var(--paper); }
  .card--back .brand {
    position: absolute;
    left: 26px;
    bottom: 44px;
    color: var(--lime-deep);
    gap: 7px;
  }
  .card--back .brand__dot { width: 8px; height: 8px; }
  .card--back .brand__name { font-size: 17px; letter-spacing: -0.2px; }

  .divider {
    position: absolute;
    left: 238px;
    top: 66px;
    width: 1px;
    height: 210px;
    background: var(--rule);
  }
  .divider__mark {
    position: absolute;
    left: -2px;
    top: 0;
    width: 5px;
    height: 28px;
    background: var(--leaf-dark);
  }
  .details {
    position: absolute;
    left: 258px;
    top: 64px;
  }
  .details__name {
    font-size: 21px;
    font-weight: 400;
    color: var(--leaf);
    letter-spacing: 0.5px;
    text-transform: uppercase;
    margin-bottom: 30px;
  }
  .contact { list-style: none; }
  .contact__item {
    display: flex;
    align-items: center;
    gap: 12px;
    font-size: 12.5px;
    color: var(--text-soft);
    margin-bottom: 16px;
    white-space: nowrap;
  }
  .contact__icon {
    width: 12px;
    height: 12px;
    flex: none;
    fill: var(--leaf);
  }
  .band {
    position: absolute;
    left: 0;
    right: 0;
    bottom: 0;
    height: 14px;
    background: var(--lime);
  }
</style>
</head>
<body>
<main class="sheet">
  <section class="card card--front" aria-label="Card front">
    <div class="brand">
      <span class="brand__dot"></span>
      <span class="brand__name">Ferncrest Dental, LLC</span>
    </div>
  </section>

  <section class="card card--back" aria-label="Card back">
    <div class="brand">
      <span class="brand__dot"></span>
      <span class="brand__name">Ferncrest Dental, LLC</span>
    </div>

    <div class="divider"><span class="divider__mark"></span></div>

    <div class="details">
      <h1 class="details__name">Dr. Lorna Pettigrew</h1>
      <ul class="contact">
        <li class="contact__item">
          <svg class="contact__icon" viewBox="0 0 24 24" aria-hidden="true"><path d="M6.6 10.8a15.1 15.1 0 0 0 6.6 6.6l2.2-2.2a1 1 0 0 1 1-.25 11.4 11.4 0 0 0 3.6.57 1 1 0 0 1 1 1V20a1 1 0 0 1-1 1A17 17 0 0 1 3 4a1 1 0 0 1 1-1h3.5a1 1 0 0 1 1 1c0 1.25.2 2.45.57 3.6a1 1 0 0 1-.25 1z"/></svg>
          <span>555-555-0193</span>
        </li>
        <li class="contact__item">
          <svg class="contact__icon" viewBox="0 0 24 24" aria-hidden="true"><path d="M2 5h20v2.2l-10 7-10-7z"/><path d="M2 9.4l10 7 10-7V19H2z"/></svg>
          <span>ferncrestdental.office@examplemail.test</span>
        </li>
        <li class="contact__item">
          <svg class="contact__icon" viewBox="0 0 24 24" aria-hidden="true"><path d="M12 2a7 7 0 0 0-7 7c0 5.2 7 13 7 13s7-7.8 7-13a7 7 0 0 0-7-7zm0 9.5A2.5 2.5 0 1 1 12 6.5a2.5 2.5 0 0 1 0 5z"/></svg>
          <span>2871 Marlowe Street Harlow Ridge, VT 05999</span>
        </li>
      </ul>
    </div>

    <div class="band"></div>
  </section>
</main>
</body>
</html>
```